Updated Stationary needed using new logo for Hair Tissue Mineral Analysis Company

Simple stationary design needed using new logo!
1. 8.5" x 11" Letterhead with company information listed below
2. 8.5" x 11" Design with Footer only with logo and information for print materials
3. 5.5" x 8.5" letterhead design
4. 4.125" x 9.5" Business envelope (#10 envelope) with address
5. 4.125" x 9.5" Business envelope with clear window (#10 envelope) with address
6. 6.5" x 9.5" envelope (6 3/4 Booklet envelope) with address
7. 10" x 13" Open End envelope
Address:
4817 N. Corwin Street
Larkfield, NV 89514
Phone:
(738)-417-3926
Website:
www.pexumor.com
Email:
information@pexumor.com
Updates
Need extra days to review
Focused on completing other projects first
Look and feel
Each slider illustrates characteristics of the customer's brand and the style your logo design should communicate.

```html
<!DOCTYPE html>
<html lang="en">
<head>
<meta charset="utf-8">
<title>Pexumor Labs – Stationery Set</title>
<link href="https://fonts.googleapis.com/css2?family=Saira+Semi+Condensed:wght@500;600&display=swap" rel="stylesheet">
<style>
  :root{
    --teal:#48bec3;
    --paper:#ffffff;
    --brand-blue:#2e5a9f;
    --navy:#13204c;
    --orange:#f5832a;
    --ink-light:#ffffff;
  }
  *{box-sizing:border-box;margin:0;padding:0}
  html,body{width:1200px;height:719px;overflow:hidden;background:var(--teal)}
  body{position:relative;font-family:"Saira Semi Condensed",Arial,sans-serif}
  .sheet{position:absolute;background:var(--paper);overflow:hidden}
  .sheet > svg.bands{position:absolute;left:0;top:0}
  .brand{position:absolute;display:flex;align-items:center;gap:.35em;white-space:nowrap;
    color:var(--brand-blue);font-weight:600;letter-spacing:.05em;text-transform:uppercase;line-height:1}
  .brand-dot{width:.8em;height:.8em;border-radius:50%;background:var(--orange);flex:none}
  .contact{position:absolute;display:flex;align-items:center;gap:.55em;white-space:nowrap;
    color:var(--ink-light);font-weight:500;line-height:1;transform:translateY(-50%)}
  .ico{width:.95em;height:.95em;flex:none}
  .ico circle{fill:none;stroke:var(--orange);stroke-width:1.4}
  .ico .core{fill:var(--orange);stroke:none}
  .addr{position:absolute;display:flex;align-items:center;gap:.55em;color:var(--ink-light);
    font-weight:500;line-height:1.15;text-align:right;white-space:nowrap;transform:translateY(-50%)}
  .window{position:absolute;background:var(--brand-blue);border-radius:7px}
</style>
</head>
<body>

<!-- Letterhead 8.5 x 11 -->
<section class="sheet letterhead" style="left:28px;top:31px;width:325px;height:420px">
  <svg class="bands" width="325" height="420" viewBox="0 0 325 420">
    <rect x="0" y="397" width="325" height="23" fill="var(--brand-blue)"/>
    <path d="M159 420 C200 375 260 358 325 357 L325 420 Z" fill="var(--orange)"/>
    <path d="M191 420 C230 385 275 366 325 364 L325 420 Z" fill="var(--navy)"/>
  </svg>
  <div class="brand" style="left:14px;top:17px;font-size:13px"><span class="brand-dot"></span>Pexumor Labs</div>
  <div class="contact" style="left:13px;top:406px;font-size:6.3px"><svg class="ico" viewBox="0 0 10 10"><circle cx="5" cy="5" r="4"/><circle class="core" cx="5" cy="5" r="1.6"/></svg>information@pexumor.com</div>
  <div class="contact" style="left:107px;top:406px;font-size:6.3px"><svg class="ico" viewBox="0 0 10 10"><circle cx="5" cy="5" r="4"/><circle class="core" cx="5" cy="5" r="1.6"/></svg>(738)-417-3926</div>
  <div class="contact" style="right:12px;top:388px;font-size:6.3px">www.pexumor.com<svg class="ico" viewBox="0 0 10 10"><circle cx="5" cy="5" r="4"/><circle class="core" cx="5" cy="5" r="1.6"/></svg></div>
  <div class="addr" style="right:12px;top:403px;font-size:6.3px"><span>4817 N. Corwin Street<br>Larkfield, NV 89514</span><svg class="ico" viewBox="0 0 10 10"><circle cx="5" cy="5" r="4"/><circle class="core" cx="5" cy="5" r="1.6"/></svg></div>
</section>

<!-- Footer-only sheet 8.5 x 11 -->
<section class="sheet footer-sheet" style="left:387px;top:31px;width:325px;height:420px">
  <svg class="bands" width="325" height="420" viewBox="0 0 325 420">
    <rect x="0" y="397" width="325" height="23" fill="var(--brand-blue)"/>
    <path d="M157 420 C200 372 258 352 325 351 L325 420 Z" fill="var(--orange)"/>
    <path d="M192 420 C230 383 275 362 325 359 L325 420 Z" fill="var(--navy)"/>
  </svg>
  <div class="brand" style="left:14px;top:376px;font-size:13px"><span class="brand-dot"></span>Pexumor Labs</div>
  <div class="contact" style="left:13px;top:406px;font-size:6.3px"><svg class="ico" viewBox="0 0 10 10"><circle cx="5" cy="5" r="4"/><circle class="core" cx="5" cy="5" r="1.6"/></svg>information@pexumor.com</div>
  <div class="contact" style="left:107px;top:406px;font-size:6.3px"><svg class="ico" viewBox="0 0 10 10"><circle cx="5" cy="5" r="4"/><circle class="core" cx="5" cy="5" r="1.6"/></svg>(738)-417-3926</div>
  <div class="contact" style="right:12px;top:389px;font-size:6.3px">www.pexumor.com<svg class="ico" viewBox="0 0 10 10"><circle cx="5" cy="5" r="4"/><circle class="core" cx="5" cy="5" r="1.6"/></svg></div>
  <div class="addr" style="right:12px;top:404px;font-size:6.3px"><span>4817 N. Corwin Street<br>Larkfield, NV 89514</span><svg class="ico" viewBox="0 0 10 10"><circle cx="5" cy="5" r="4"/><circle class="core" cx="5" cy="5" r="1.6"/></svg></div>
</section>

<!-- Booklet envelope 6.5 x 9.5 -->
<section class="sheet envelope-booklet" style="left:767px;top:31px;width:363px;height:248px">
  <svg class="bands" width="363" height="248" viewBox="0 0 363 248">
    <rect x="0" y="223" width="363" height="25" fill="var(--brand-blue)"/>
    <path d="M144 248 C195 185 270 155 363 152 L363 248 Z" fill="var(--orange)"/>
    <path d="M194 248 C240 195 300 168 363 165 L363 248 Z" fill="var(--navy)"/>
  </svg>
  <div class="brand" style="right:15px;top:12px;font-size:15px"><span class="brand-dot"></span>Pexumor Labs</div>
  <div class="contact" style="right:16px;top:191px;font-size:7.4px">(738)-417-3926<svg class="ico" viewBox="0 0 10 10"><circle cx="5" cy="5" r="4"/><circle class="core" cx="5" cy="5" r="1.6"/></svg></div>
  <div class="contact" style="right:16px;top:202px;font-size:7.4px">www.pexumor.com<svg class="ico" viewBox="0 0 10 10"><circle cx="5" cy="5" r="4"/><circle class="core" cx="5" cy="5" r="1.6"/></svg></div>
  <div class="contact" style="right:16px;top:213px;font-size:7.4px">information@pexumor.com<svg class="ico" viewBox="0 0 10 10"><circle cx="5" cy="5" r="4"/><circle class="core" cx="5" cy="5" r="1.6"/></svg></div>
  <div class="addr" style="right:16px;top:229px;font-size:7.4px"><span>4817 N. Corwin Street<br>Larkfield, NV 89514</span><svg class="ico" viewBox="0 0 10 10" style="align-self:flex-start"><circle cx="5" cy="5" r="4"/><circle class="core" cx="5" cy="5" r="1.6"/></svg></div>
</section>

<!-- #10 envelope -->
<section class="sheet envelope-10" style="left:38px;top:527px;width:363px;height:158px">
  <svg class="bands" width="363" height="158" viewBox="0 0 363 158">
    <rect x="0" y="136" width="363" height="22" fill="var(--brand-blue)"/>
    <path d="M151 158 C200 100 270 68 363 65 L363 158 Z" fill="var(--orange)"/>
    <path d="M201 158 C245 110 300 82 363 78 L363 158 Z" fill="var(--navy)"/>
  </svg>
  <div class="brand" style="right:12px;top:13px;font-size:15px"><span class="brand-dot"></span>Pexumor Labs</div>
  <div class="contact" style="right:12px;top:104px;font-size:7.4px">(738)-417-3926<svg class="ico" viewBox="0 0 10 10"><circle cx="5" cy="5" r="4"/><circle class="core" cx="5" cy="5" r="1.6"/></svg></div>
  <div class="contact" style="right:12px;top:115px;font-size:7.4px">www.pexumor.com<svg class="ico" viewBox="0 0 10 10"><circle cx="5" cy="5" r="4"/><circle class="core" cx="5" cy="5" r="1.6"/></svg></div>
  <div class="contact" style="right:12px;top:126px;font-size:7.4px">information@pexumor.com<svg class="ico" viewBox="0 0 10 10"><circle cx="5" cy="5" r="4"/><circle class="core" cx="5" cy="5" r="1.6"/></svg></div>
  <div class="addr" style="right:12px;top:143px;font-size:7.4px"><span>4817 N. Corwin Street<br>Larkfield, NV 89514</span><svg class="ico" viewBox="0 0 10 10" style="align-self:flex-start"><circle cx="5" cy="5" r="4"/><circle class="core" cx="5" cy="5" r="1.6"/></svg></div>
</section>

<!-- #10 window envelope -->
<section class="sheet envelope-window" style="left:468px;top:527px;width:363px;height:158px">
  <svg class="bands" width="363" height="158" viewBox="0 0 363 158">
    <rect x="0" y="133" width="363" height="25" fill="var(--brand-blue)"/>
    <path d="M149 158 C200 98 270 66 363 63 L363 158 Z" fill="var(--orange)"/>
    <path d="M200 158 C245 108 300 81 363 77 L363 158 Z" fill="var(--navy)"/>
  </svg>
  <div class="window" style="left:22px;top:33px;width:164px;height:73px"></div>
  <div class="brand" style="right:14px;top:22px;font-size:15px"><span class="brand-dot"></span>Pexumor Labs</div>
  <div class="contact" style="right:12px;top:102px;font-size:7.4px">(738)-417-3926<svg class="ico" viewBox="0 0 10 10"><circle cx="5" cy="5" r="4"/><circle class="core" cx="5" cy="5" r="1.6"/></svg></div>
  <div class="contact" style="right:12px;top:113px;font-size:7.4px">www.pexumor.com<svg class="ico" viewBox="0 0 10 10"><circle cx="5" cy="5" r="4"/><circle class="core" cx="5" cy="5" r="1.6"/></svg></div>
  <div class="contact" style="right:12px;top:124px;font-size:7.4px">information@pexumor.com<svg class="ico" viewBox="0 0 10 10"><circle cx="5" cy="5" r="4"/><circle class="core" cx="5" cy="5" r="1.6"/></svg></div>
  <div class="addr" style="right:12px;top:140px;font-size:7.4px"><span>4817 N. Corwin Street<br>Larkfield, NV 89514</span><svg class="ico" viewBox="0 0 10 10" style="align-self:flex-start"><circle cx="5" cy="5" r="4"/><circle class="core" cx="5" cy="5" r="1.6"/></svg></div>
</section>

<!-- Letterhead 5.5 x 8.5 -->
<section class="sheet letterhead-small" style="left:949px;top:377px;width:210px;height:325px">
  <svg class="bands" width="210" height="325" viewBox="0 0 210 325">
    <rect x="0" y="311" width="210" height="14" fill="var(--brand-blue)"/>
    <path d="M107 325 C130 298 165 286 210 284 L210 325 Z" fill="var(--orange)"/>
    <path d="M134 325 C155 304 180 293 210 292 L210 325 Z" fill="var(--navy)"/>
  </svg>
  <div class="brand" style="left:12px;top:13px;font-size:9.5px"><span class="brand-dot"></span>Pexumor Labs</div>
  <div class="contact" style="left:6px;top:318px;font-size:3.8px"><svg class="ico" viewBox="0 0 10 10"><circle cx="5" cy="5" r="4"/><circle class="core" cx="5" cy="5" r="1.6"/></svg>information@pexumor.com</div>
  <div class="contact" style="left:68px;top:318px;font-size:3.8px"><svg class="ico" viewBox="0 0 10 10"><circle cx="5" cy="5" r="4"/><circle class="core" cx="5" cy="5" r="1.6"/></svg>(738)-417-3926</div>
  <div class="contact" style="right:6px;top:305px;font-size:3.8px">www.pexumor.com<svg class="ico" viewBox="0 0 10 10"><circle cx="5" cy="5" r="4"/><circle class="core" cx="5" cy="5" r="1.6"/></svg></div>
  <div class="addr" style="right:6px;top:315px;font-size:3.8px"><span>4817 N. Corwin Street<br>Larkfield, NV 89514</span><svg class="ico" viewBox="0 0 10 10"><circle cx="5" cy="5" r="4"/><circle class="core" cx="5" cy="5" r="1.6"/></svg></div>
</section>

</body>
</html>
```